Broschüren-Design für Produzent von hochwertigen Verpackungs- und Präsentationslösungen
Zielgruppe
Wir produzieren hochwertige Verpackungs- und Präsentationslösungen.
Unsere Zielgruppe sind Firmen, welche kreative Premium-Packaging benötigt.
Aufgabenstellung
- Format: A4 hoch
- Umfang: 6 Seiten
- Falzart: Wickelfalz
- Design muss sehr hochwertig sein. Passend zu unseren Produktion (siehe Bilder)
- Wir möchten mit diesem Falzprospekt eine Übersicht über unsere Produkte generieren.
- Die Produkte sind bereits schon hochwertig fotografiert und müssen in einem anspruchsvollen Design in Szene gesetzt werden.
- Der Prospekt sollte die Kunden emotional berühren.
- Auf der Titelseite werden wir den Titel «High Performance Packaging» mit Folien prägen
- Seitenaufbau gemäss meiner Visualisierung (im Anhang)
- Bei jeder Produktkategorie möchte ich ein Grosses Übersichtsbild zusammen mit einem kurzen Text.
Ergänzend können noch weitere (passende) Bilder der jeweiligen Kategorie abgebildet werden.
Im Anhang finden Sie:
- Visualisierung des zu gestaltenden Prospekt
- Werbeflyer (zur Ansicht/Inspiration). In etwa so stellen wir uns das Design/Tonalität vor.
- Weitere passende Produktbilder können vorerst auf der Webseite unseres Produktionspartner (www.bogenhaus.de) entnommen werden.

```html
<!DOCTYPE html>
<html lang="de">
<head>
<meta charset="utf-8">
<title>Falzprospekt – Innenseiten</title>
<link href="https://fonts.googleapis.com/css2?family=Poppins:wght@300;400;600&display=swap" rel="stylesheet">
<style>
  :root {
    --backdrop: #e9e9ea;
    --page-grey: #c8c8ca;
    --page-light: #f2f2f2;
    --page-white: #fbfbfb;
    --navy: #3a3f4e;
    --brown: #7e5f57;
    --ink: #2e2e33;
    --ink-soft: #8a8a90;
    --ink-on-dark: #e6e8ee;
    --ink-on-dark-soft: #a6abba;
    --rule: #b9b9bd;
    --photo-dark-a: #2c2d31;
    --photo-dark-b: #45464c;
    --photo-mid-a: #55565c;
    --photo-mid-b: #7a7b81;
    --photo-light-a: #d7d8dd;
    --photo-light-b: #eeeef1;
  }
  * { margin: 0; padding: 0; box-sizing: border-box; }
  html, body { width: 1200px; height: 804px; overflow: hidden; }
  body {
    background: var(--backdrop);
    font-family: "Poppins", sans-serif;
    position: relative;
  }
  .spread {
    position: absolute;
    left: 60px; top: 147px;
    width: 1080px; height: 509px;
    display: flex;
    box-shadow: 0 14px 40px rgba(0,0,0,.12);
  }
  .page { position: relative; width: 360px; height: 509px; overflow: hidden; }
  .page--grey { background: var(--page-grey); }
  .page--light { background: var(--page-light); }
  .page--brown { background: var(--brown); }

  .photo { position: absolute; }
  .photo--dark { background: linear-gradient(180deg, var(--photo-dark-b), var(--photo-dark-a)); }
  .photo--mid { background: linear-gradient(180deg, var(--photo-mid-b), var(--photo-mid-a)); }
  .photo--light { background: linear-gradient(180deg, var(--photo-light-b), var(--photo-light-a)); }

  .text-col { position: absolute; }
  .text-col--navy { background: var(--navy); }
  .entry { padding: 0 0 14px; margin-bottom: 16px; border-bottom: 1px dashed var(--rule); }
  .entry:last-child { border-bottom: none; }
  .entry__title { font-size: 9px; font-weight: 600; letter-spacing: .04em; margin-bottom: 7px; color: var(--ink); }
  .entry__body { font-size: 6.4px; font-weight: 300; line-height: 1.6; color: var(--ink-soft); }
  .text-col--navy .entry__title { color: var(--ink-on-dark); }
  .text-col--navy .entry__body { color: var(--ink-on-dark-soft); }
  .text-col--navy .entry { border-bottom-color: #6b7082; }

  .page-letter {
    position: absolute; right: 14px; bottom: 10px;
    font-size: 12px; font-weight: 600; color: rgba(255,255,255,.7);
  }
  .page--light .page-letter { color: #d2d2d4; }

  .brown-body { position: absolute; left: 0; top: 60px; width: 360px; height: 389px; background: var(--page-white); }
</style>
</head>
<body>
<main class="spread">

  <section class="page page--grey">
    <div class="photo photo--dark" style="left:16px; top:56px; width:184px; height:140px;" role="img" aria-label="Produktfoto: Verpackungsbox mit Schreibgerät auf dunklem Grund"></div>
    <div class="photo photo--dark" style="left:16px; top:196px; width:184px; height:136px;" role="img" aria-label="Produktfoto: rote und dunkelblaue Präsentationsmappen"></div>
    <div class="photo photo--dark" style="left:16px; top:332px; width:184px; height:136px;" role="img" aria-label="Produktfoto: Mustermappen mit Materialproben"></div>
    <div class="text-col text-col--navy" style="left:200px; top:56px; width:160px; height:412px; padding:28px 16px 0 18px;">
      <article class="entry">
        <h2 class="entry__title">VERPACKUNGEN</h2>
        <p class="entry__body">Präsentationsmappen Lorem ipsum dolor sit amet, consetetur sadipscing elitr, sed diam nonumy eirmod tempor invidunt ut labore et dolore magna aliquyam erat, sed diam voluptua. At vero eos et accusam et justo duo dolores et ea rebum. Stet clita kasd.</p>
      </article>
      <article class="entry">
        <h2 class="entry__title">PRÄSENTATIONSMAPPEN</h2>
        <p class="entry__body">Präsentationsmappen Lorem ipsum dolor sit amet, consetetur sadipscing elitr, sed diam nonumy eirmod tempor invidunt ut labore et dolore magna aliquyam erat, sed diam voluptua. At vero eos et accusam et justo duo dolores et ea rebum. Stet clita kasd.</p>
      </article>
      <article class="entry">
        <h2 class="entry__title">MUSTERMAPPEN</h2>
        <p class="entry__body">Präsentationsmappen Lorem ipsum dolor sit amet, consetetur sadipscing elitr, sed diam nonumy eirmod tempor invidunt ut labore et dolore magna aliquyam erat, sed diam voluptua. At vero eos et accusam et justo duo dolores et ea rebum. Stet clita kasd.</p>
      </article>
    </div>
    <span class="page-letter">D</span>
  </section>

  <section class="page page--light">
    <div class="photo photo--dark" style="left:0; top:70px; width:190px; height:124px;" role="img" aria-label="Produktfoto: Ringordner in hellen Farbtönen"></div>
    <div class="photo photo--light" style="left:0; top:194px; width:190px; height:124px;" role="img" aria-label="Produktfoto: Schuber mit farbigen Ordnern"></div>
    <div class="photo photo--dark" style="left:0; top:318px; width:190px; height:124px;" role="img" aria-label="Produktfoto: dunkle Schreibmappe mit Block und Stift"></div>
    <div class="text-col" style="left:210px; top:76px; width:132px;">
      <article class="entry">
        <h2 class="entry__title">RINGORDNER</h2>
        <p class="entry__body">Präsentationsmappen Lorem ipsum dolor sit amet, consetetur sadipscing elitr, sed diam nonumy eirmod tempor invidunt ut labore et dolore magna aliquyam erat, sed diam voluptua. At vero eos et accusam et justo duo dolores et ea rebum. Stet clita kasd.</p>
      </article>
      <article class="entry">
        <h2 class="entry__title">SCHUBER</h2>
        <p class="entry__body">Präsentationsmappen Lorem ipsum dolor sit amet, consetetur sadipscing elitr, sed diam nonumy eirmod tempor invidunt ut labore et dolore magna aliquyam erat, sed diam voluptua. At vero eos et accusam et justo duo dolores et ea rebum. Stet clita kasd.</p>
      </article>
      <article class="entry">
        <h2 class="entry__title">SCHREIBMAPPEN</h2>
        <p class="entry__body">Präsentationsmappen Lorem ipsum dolor sit amet, consetetur sadipscing elitr, sed diam nonumy eirmod tempor invidunt ut labore et dolore magna aliquyam erat, sed diam voluptua. At vero eos et accusam et justo duo dolores et ea rebum. Stet clita kasd.</p>
      </article>
    </div>
    <span class="page-letter">E</span>
  </section>

  <section class="page page--brown">
    <div class="brown-body"></div>
    <div class="photo photo--mid" style="left:22px; top:110px; width:196px; height:256px;" role="img" aria-label="Produktfotos: aufgestellte graue Fächermappe und geöffneter grauer Präsentationskoffer"></div>
    <div class="text-col" style="left:232px; top:114px; width:112px;">
      <article class="entry">
        <h2 class="entry__title">FÄCHERMAPPEN</h2>
        <p class="entry__body">Präsentationsmappen Lorem ipsum dolor sit amet, consetetur sadipscing elitr, sed diam nonumy eirmod tempor invidunt ut labore et dolore magna aliquyam erat, sed diam voluptua. At vero eos et accusam et justo duo dolores et ea rebum. Stet clita kasd.</p>
      </article>
      <article class="entry">
        <h2 class="entry__title">PRÄSENTATIONSKOFFER</h2>
        <p class="entry__body">Präsentationsmappen Lorem ipsum dolor sit amet, consetetur sadipscing elitr, sed diam nonumy eirmod tempor invidunt ut labore et dolore magna aliquyam erat, sed diam voluptua. At vero eos et accusam et justo duo dolores et ea rebum. Stet clita kasd.</p>
      </article>
    </div>
  </section>

</main>
</body>
</html>
```